International Dating Community Needs a Web Design

We need a single page web design built on plomet.com. Designers need to design a one page web design on PLOMET, take a screenshot and paste it here. Once the winner is chosen, the designer needs to give me access to the design and transfer over the implementation.
REQUIREMENTS:
- Designer MUST design on plomet.com (http://www.plomet.com/support/main/html5/getting-started/signing-free)
- Once designed, designer needs to take a screenshot of the plomet design and submit the design on artvessel.
- Please add the site url as the design comment when you submit the design
- Any designers that use existing PLOMET templates will NOT be eligible to win and will be eliminated.
Note: If you use any stock images, simply let me know the numbers and I will purchase them.
PAGE INFORMATION:
Color Scheme:
- Light Blue / Cyan
- White
- Black / Dark Gray
Header:
- Logo (attached) on the left
- Login / Register on the right
Navigation bar:
- Home
- Events
- Entertainment / Music
- Gallery
- Membership
- About Us
Homepage Content:
The worlds #1 destination for international dating!
We may be new to you, but our team have been around for longer than you think. We're here to promote upcoming cultural events in your community, promote local businesses serving your community & soon we will also be offering an online dating service to meet others within the area.
If you're interested in learning more about events & concerts relating to the community then make sure you like us on Chatterbox.
If you have any comments or feedback, we'd love to hear from you! Click here to contact us.
Photos:
Im open for you to use any photos you like - some sites I like:
http://www.openpicturebank.net/images/People_g40.html
http://www.qvr.hu/category/135

```html
<!DOCTYPE html>
<html lang="en">
<head>
<meta charset="utf-8">
<title>luvana — international dating community</title>
<link href="https://fonts.googleapis.com/css2?family=Open+Sans:wght@300;400;600;700&display=swap" rel="stylesheet">
<style>
  :root {
    --teal: #40e0d0;
    --teal-soft: #6fe6da;
    --white: #ffffff;
    --ink: #3a3a3a;
    --paper: #f3f3f3;
    --stage: #e4e2e6;
  }
  * { box-sizing: border-box; margin: 0; padding: 0; }
  html, body { width: 1200px; height: 1000px; overflow: hidden; }
  body {
    background: var(--stage);
    font-family: "Open Sans", sans-serif;
    color: var(--white);
  }
  .page {
    position: absolute; left: 180px; top: 0;
    width: 840px; height: 1000px;
    background: var(--white);
    overflow: hidden;
  }

  /* Hero */
  .hero { position: relative; height: 340px; }
  .hero-photo {
    position: absolute; inset: 0;
    background:
      linear-gradient(180deg, rgba(0,0,0,0.05), rgba(40,20,80,0.25)),
      linear-gradient(105deg, #d8b93f 0%, #c79a45 28%, #8a3f86 55%, #4a3c9e 78%, #2f4fb0 100%);
  }
  .site-nav {
    position: absolute; top: 12px; left: 170px;
    display: flex; align-items: center; gap: 14px;
  }
  .brand-box {
    background: var(--teal);
    padding: 4px 10px;
    font-weight: 400; font-size: 20px; color: var(--white);
    letter-spacing: 0.5px;
  }
  .nav-links { font-size: 10px; font-weight: 600; letter-spacing: 0.3px; }
  .hero-title { position: absolute; left: 270px; top: 40px; width: 300px; height: 210px; }
  .hero-sub {
    position: absolute; top: 226px; width: 100%; text-align: center;
    font-weight: 700; font-size: 15px;
  }
  .scroll-down {
    position: absolute; top: 284px; width: 100%; text-align: center;
    font-size: 7px; font-weight: 600;
  }
  .scroll-down svg { display: block; margin: 0 auto 3px; }

  /* About band */
  .about {
    background: var(--teal);
    height: 505px;
    text-align: center;
    padding-top: 14px;
  }
  .lead { font-weight: 700; font-size: 11px; line-height: 1.35; }
  .brand-name { font-weight: 300; font-size: 26px; margin-top: 6px; line-height: 1; }
  .brand-tag { font-weight: 300; font-size: 12px; margin-top: 2px; }
  .section-title { font-weight: 700; font-size: 10px; margin-top: 12px; letter-spacing: 0.3px; }
  .aims { position: relative; height: 120px; }
  .aims-path { position: absolute; left: 0; top: 0; }
  .aim {
    position: absolute; width: 170px; font-size: 8px; line-height: 1.35;
  }
  .aim svg { display: block; margin: 0 auto 6px; }
  .aim-events { left: 230px; top: 36px; }
  .aim-business { left: 440px; top: 36px; }
  .soon-text { font-size: 9px; margin-top: 4px; }
  .match {
    display: flex; justify-content: center; align-items: center; gap: 0;
    margin-top: 10px;
  }
  .match-person { width: 34px; height: 34px; border-radius: 50%; border: 2px solid var(--white); }
  .match-line { width: 120px; height: 1px; border-top: 1px dashed var(--white); position: relative; }
  .match-line svg { position: absolute; left: 52px; top: -8px; }
  .social-square {
    width: 26px; height: 26px; background: var(--white);
    margin: 8px auto 3px;
  }
  .social-label { font-size: 7px; }
  .social-text { font-size: 9px; line-height: 1.4; margin-top: 12px; }
  .about .scroll-down { position: static; margin-top: 12px; }

  /* Contact */
  .contact {
    background: var(--paper);
    height: 128px; text-align: center; padding-top: 12px;
    color: var(--teal);
  }
  .contact .brand-name { font-size: 22px; margin-top: 0; }
  .contact .brand-tag { font-size: 10px; }
  .contact .section-title { margin-top: 8px; font-size: 9px; }
  .contact svg { display: block; margin: 6px auto 4px; }
  .contact-note { font-size: 8px; }

  /* Footer */
  .site-footer {
    text-align: center; color: var(--ink);
    font-size: 7px; line-height: 1.6; padding-top: 4px;
  }
</style>
</head>
<body>
<main class="page">

  <header class="hero">
    <div class="hero-photo" role="img" aria-label="Photo of two young women in sunglasses posing against a yellow brick wall"></div>
    <nav class="site-nav">
      <div class="brand-box">luvana</div>
      <div class="nav-links">HOME - EVENTS - ENTERTAINMENT / MUSIC - GALLERY - MEMBERSHIP - ABOUT US</div>
    </nav>
    <svg class="hero-title" viewBox="0 0 300 210" aria-label="The worlds number one">
      <defs><path id="title-arc" d="M40 95 Q150 10 260 95"/></defs>
      <text font-family="Open Sans, sans-serif" font-weight="700" font-size="27" fill="#ffffff">
        <textPath href="#title-arc" startOffset="50%" text-anchor="middle">THE <tspan fill="#40e0d0">WORLDS</tspan> #1</textPath>
      </text>
      <path d="M150 180 C120 150 100 135 100 110 C100 92 114 82 128 82 C140 82 147 90 150 97 C153 90 160 82 172 82 C186 82 200 92 200 110 C200 135 180 150 150 180 Z" fill="#ffffff"/>
    </svg>
    <p class="hero-sub">DESTINATION FOR INTERNATIONAL DATING!</p>
    <div class="scroll-down">
      <svg width="14" height="14" viewBox="0 0 14 14"><circle cx="7" cy="7" r="6" fill="none" stroke="#fff" stroke-width="1.2"/><path d="M4 6 L7 9 L10 6" fill="none" stroke="#fff" stroke-width="1.2"/></svg>
      SCROLL DOWN
    </div>
  </header>

  <section class="about">
    <p class="lead">WE MAY BE NEW TO YOU. BUT OUR TEAM HAVE BEEN AROUND<br>FOR LONGER THAN YOU THINK.</p>
    <p class="brand-name">luvana</p>
    <p class="brand-tag">international dating community</p>
    <p class="section-title">WE'RE HERE TO</p>

    <div class="aims">
      <svg class="aims-path" width="840" height="120" viewBox="0 0 840 120">
        <path d="M420 0 C420 30 330 20 315 40 M420 0 C420 30 510 20 525 40 M420 0 L420 110" fill="none" stroke="#fff" stroke-width="1" stroke-dasharray="3 3"/>
      </svg>
      <div class="aim aim-events">
        <svg width="26" height="26" viewBox="0 0 26 26"><rect x="2" y="4" width="22" height="20" fill="none" stroke="#fff" stroke-width="1.5"/><line x1="2" y1="9" x2="24" y2="9" stroke="#fff" stroke-width="1.5"/><path d="M7 13h3M12 13h3M17 13h3M7 17h3M12 17h3M17 17h3M7 21h3M12 21h3" stroke="#fff" stroke-width="1.5"/><line x1="8" y1="2" x2="8" y2="6" stroke="#fff" stroke-width="1.5"/><line x1="18" y1="2" x2="18" y2="6" stroke="#fff" stroke-width="1.5"/></svg>
        Promote upcoming cultural<br>events in your community
      </div>
      <div class="aim aim-business">
        <svg width="26" height="26" viewBox="0 0 26 26"><rect x="6" y="2" width="14" height="22" fill="none" stroke="#fff" stroke-width="1.5"/><path d="M9 6h3M14 6h3M9 10h3M14 10h3M9 14h3M14 14h3" stroke="#fff" stroke-width="1.5"/><rect x="11" y="18" width="4" height="6" fill="#fff"/></svg>
        Promote local businesses<br>serving your community
      </div>
    </div>

    <p class="section-title">COMING SOON:</p>
    <p class="soon-text">We will also be offering an online dating service to meet others within the area</p>
    <div class="match">
      <div class="match-person" role="img" aria-label="Man icon"></div>
      <div class="match-line">
        <svg width="16" height="15" viewBox="0 0 16 15"><path d="M8 14 C4 10 1 8 1 5 C1 2.5 3 1 5 1 C6.5 1 7.5 2 8 3 C8.5 2 9.5 1 11 1 C13 1 15 2.5 15 5 C15 8 12 10 8 14 Z" fill="#fff"/></svg>
      </div>
      <div class="match-person" role="img" aria-label="Woman icon"></div>
    </div>

    <p class="section-title">LIKE US ON CHATTERBOX</p>
    <div class="social-square"></div>
    <p class="social-label">Chatterbox</p>
    <p class="social-text">If you're interested in learning more about<br>events &amp; concerts relating to the community.</p>
    <div class="scroll-down">
      <svg width="12" height="12" viewBox="0 0 14 14"><circle cx="7" cy="7" r="6" fill="none" stroke="#fff" stroke-width="1.2"/><path d="M4 6 L7 9 L10 6" fill="none" stroke="#fff" stroke-width="1.2"/></svg>
      SCROLL DOWN
    </div>
  </section>

  <section class="contact">
    <p class="brand-name">luvana</p>
    <p class="brand-tag">international dating community</p>
    <p class="section-title">CONTACT US</p>
    <svg width="26" height="18" viewBox="0 0 26 18"><rect x="0" y="0" width="26" height="18" fill="#40e0d0"/><path d="M1 1 L13 10 L25 1" fill="none" stroke="#fff" stroke-width="1.5"/></svg>
    <p class="contact-note">If you have any comments or feedback, we'd love to hear from you.</p>
  </section>

  <footer class="site-footer">
    <p>luvana. Copyright 2014. All rights reserved.</p>
    <p>Design and build by the luvana team</p>
  </footer>

</main>
</body>
</html>
```